Professional / Luxury Rack Card Design Needed (Do not use AI)

We are a private, boutique style optometry practice in College Station, Texas. We want the new design to communicate a premium, modern, luxury eye care experience while remaining professional and approachable.
When someone picks up this rack card, we want them to think:
"This practice looks modern, advanced, trustworthy, and premium. I would expect exceptional care and a high-end eyewear experience."

Target Market(s)

Families, professionals, adults seeking comprehensive medical eye care and vision correction. Patients seeking premium eyewear, advanced technology, and personalize care. Individuals and families seeking long term relationships with a trusted eye care provider. Patients who value exceptional service, expertise, and convenience.

Industry/Entity Type

Medical & Optometry-luxury optical

Font styles to use
Serif
Other font styles liked:
• Avenir if available. If not, Montserrat for headlines and Open Sans for Body text. For the slogan, use larger bold Montserrat.

Requirements
Must have
• Non-edited photo of doctors (merged together) with names. "Your Vision. Our Focus." Phone, website, Text/Call to Schedule appointment (Call to action to schedule). Accepting new patients. Eye Care center logo prominently displayed. Real photo of Eye Care Center building. Contact information (see attachement with all info)
Nice to have
• For frame brands, use the branded names. (see attachment)
Should not have
• Shouild not be busy/cluttered. Do not use scripted font from my website. Do NOT use AI generated images. Do not edit doctor faces other than merging them together. DO NOT use AI to edit faces....only to merge them side by side.

```html
<!DOCTYPE html>
<html lang="en">
<head>
<meta charset="utf-8">
<title>Clearview Eye Studio Rack Card</title>
<link href="https://fonts.googleapis.com/css2?family=Signika:wght@300;400;600;700&family=Open+Sans:wght@400;600&display=swap" rel="stylesheet">
<style>
:root{
  --navy:#1f3b53;
  --gold:#d9b125;
  --ice:#d4eaf3;
  --white:#ffffff;
  --ink:#1b2a36;
  --rule:#9fb4c2;
  --stripe-grey:#8e98a2;
  --stripe-brown:#7a3a1c;
  --stripe-green:#8a9a3a;
  --stripe-blue:#8fc5d6;
}
*{box-sizing:border-box;margin:0;padding:0}
html,body{width:1200px;height:768px;overflow:hidden;background:#fff}
body{position:relative;font-family:"Signika",sans-serif;color:var(--ink)}
.side-label{position:absolute;top:20px;width:295px;text-align:center;font:400 15px "Open Sans",sans-serif;color:#222}
.card{position:absolute;top:54px;width:295px;height:662px;overflow:hidden;background:var(--white);box-shadow:0 1px 4px rgba(0,0,0,.25)}
.card-front{left:250px}
.card-back{left:655px;background:var(--ice)}
.abs{position:absolute}
.photo{position:absolute;left:0;width:100%}
/* front */
.building-photo{top:55px;height:155px;background:linear-gradient(180deg,#8fb0cc 0%,#d9c9a0 45%,#a28357 100%)}
.header-wave{top:0;left:0}
.logo{top:16px;left:18px;display:flex;align-items:center;gap:10px}
.logo-mark{width:38px;height:38px;border-radius:50%;border:3px solid var(--stripe-blue)}
.logo-name{font:400 21px "Signika",sans-serif;color:var(--white);line-height:1;white-space:nowrap}
.logo-sub{font:400 8px "Signika",sans-serif;color:var(--white);letter-spacing:1.5px;margin-top:6px;border-top:1px solid rgba(255,255,255,.6);padding-top:4px;white-space:nowrap}
.photo-wave{top:184px;left:0}
.slogan{top:210px;width:100%;text-align:center;line-height:1}
.slogan-line1{font:400 31px "Signika",sans-serif;color:var(--navy)}
.slogan-line2{font:700 31px "Signika",sans-serif;color:var(--gold);margin-top:1px}
.interior-photo{top:279px;height:156px;background:linear-gradient(160deg,#6d5a48 0%,#3c3430 50%,#7d6a55 100%)}
.pillars{top:435px;height:71px;width:100%;background:var(--ice);display:flex}
.pillar{flex:1;text-align:center;padding-top:4px;font:300 13px/14px "Signika",sans-serif;color:var(--navy)}
.pillar+.pillar{border-left:1.5px solid var(--gold)}
.pillar svg{display:block;margin:0 auto 3px}
.frames-row{top:506px;height:27px;width:100%;background:var(--ice);border-top:1.5px solid var(--gold);display:flex;align-items:center;justify-content:center;gap:4px;font:400 13px "Signika",sans-serif;color:var(--navy);white-space:nowrap}
.frames-row b{color:var(--gold);font-weight:600}
.brands{top:540px;left:10px;width:276px;display:grid;grid-template-columns:1fr 1fr 1fr 1.4fr;row-gap:1px;text-align:center;font:400 9px/17px "Open Sans",sans-serif;color:#222;white-space:nowrap}
.brands span:nth-child(odd){font-family:"Signika",sans-serif;font-weight:600;letter-spacing:.5px}
.contact-band{top:594px;height:58px;width:100%;background:var(--navy)}
.site{top:3px;width:100%;text-align:center;font:700 18px "Signika",sans-serif;color:var(--gold)}
.contact-rule{top:26px;left:0;width:100%;height:1.5px;background:var(--gold)}
.cta{top:30px;left:30px;width:102px;text-align:center;font:400 10.5px/12px "Signika",sans-serif;color:var(--gold)}
.phone{top:30px;left:118px;width:148px;text-align:center;font:600 19px "Signika",sans-serif;color:var(--white)}
.stripe{bottom:0;left:0;width:100%;height:10px;display:flex}
.stripe i{flex:1}
/* back */
.gold-wave{top:0;left:0}
.back-title{top:9px;width:100%;text-align:center;font:700 19px "Signika",sans-serif;color:var(--navy)}
.doctor{position:absolute;width:140px;text-align:center;font:400 11px "Signika",sans-serif;color:var(--ink);white-space:nowrap}
.doctor-photo{width:112px;height:112px;margin:0 auto 4px;border-radius:50%;border:3px solid var(--white);background:radial-gradient(circle at 50% 45%,#c9b49a 0%,#8a7760 70%,#5c4f42 100%)}
.services-band{top:305px;height:31px;width:100%;background:var(--gold);text-align:center;font:700 19px/31px "Signika",sans-serif;color:var(--navy)}
.services{top:338px;left:12px;width:273px;display:grid;grid-template-columns:1fr 1fr;column-gap:8px}
.service{display:flex;align-items:center;gap:8px;height:30px;border-bottom:1px solid var(--rule);font:400 10px/11px "Open Sans",sans-serif;color:var(--ink)}
.service.tall{height:36px;border-bottom:none}
.service svg{flex:none}
.navy-base{top:522px;height:96px;width:100%;background:var(--navy)}
.feature-box{top:495px;left:22px;width:251px;height:72px;background:var(--white);border:1.5px solid var(--navy);border-radius:10px;display:flex;align-items:center}
.feature{flex:1;text-align:center;font:400 7.5px/10px "Signika",sans-serif;color:var(--ink);text-transform:uppercase}
.feature+.feature{border-left:1px solid var(--gold)}
.feature svg{display:block;margin:0 auto 4px}
.address{top:574px;width:100%;text-align:center;font:400 11px "Signika",sans-serif;color:var(--white)}
.hours{top:595px;width:100%;text-align:center;font:700 15px "Signika",sans-serif;color:var(--gold);white-space:nowrap}
.tagline{top:618px;height:34px;width:100%;background:var(--white);text-align:center;font:700 14px/34px "Signika",sans-serif;color:var(--navy)}
</style>
</head>
<body>

<div class="side-label" style="left:250px">Front</div>
<div class="side-label" style="left:655px">Back</div>

<section class="card card-front">
  <div class="photo building-photo" role="img" aria-label="Photo of the eye care studio building exterior with arched windows and tiled roof"></div>
  <svg class="abs header-wave" width="295" height="100" viewBox="0 0 295 100">
    <path d="M0 0H295V72C270 64 255 88 228 84C200 80 190 62 160 70C130 78 118 92 90 86C60 80 40 66 20 72C10 75 4 76 0 76Z" fill="var(--navy)"/>
  </svg>
  <div class="abs logo">
    <div class="logo-mark"></div>
    <div>
      <div class="logo-name">Clearview Eye Studio</div>
      <div class="logo-sub">A MEMBER OF OPTIC ALLIANCE</div>
    </div>
  </div>
  <svg class="abs photo-wave" width="295" height="30" viewBox="0 0 295 30">
    <path d="M0 30V14C20 4 40 2 62 10C84 18 100 6 124 8C150 10 170 22 196 16C222 10 250 2 272 12C284 18 290 20 295 20V30Z" fill="var(--white)"/>
  </svg>
  <div class="abs slogan">
    <div class="slogan-line1">Your Vision.</div>
    <div class="slogan-line2">Our Focus.</div>
  </div>
  <div class="photo interior-photo" role="img" aria-label="Photo of the studio interior with stone wall, reception desk and eyewear displays"></div>

  <div class="abs pillars">
    <div class="pillar">
      <svg width="42" height="30" viewBox="0 0 42 30"><path d="M2 15C10 4 32 4 40 15C32 26 10 26 2 15Z" fill="none" stroke="var(--navy)" stroke-width="2.5"/><circle cx="21" cy="15" r="8" fill="var(--navy)"/><path d="M21 10V20M16 15H26" stroke="#fff" stroke-width="2.5"/></svg>
      Comprehensive<br>Eye Care
    </div>
    <div class="pillar">
      <svg width="36" height="32" viewBox="0 0 36 32"><rect x="4" y="2" width="28" height="20" rx="2" fill="none" stroke="var(--navy)" stroke-width="2.5"/><circle cx="18" cy="12" r="5" fill="none" stroke="var(--navy)" stroke-width="2"/><path d="M12 22V27H24V22M8 30H28" stroke="var(--navy)" stroke-width="2.5" fill="none"/></svg>
      Advanced<br>Technology
    </div>
    <div class="pillar">
      <svg width="32" height="32" viewBox="0 0 32 32"><circle cx="16" cy="7" r="6" fill="var(--navy)"/><path d="M4 30C4 20 9 15 16 15C23 15 28 20 28 30Z" fill="var(--navy)"/><path d="M16 28L10 22C8 19 12 16 16 20C20 16 24 19 22 22Z" fill="#fff"/></svg>
      Personalized<br>Care
    </div>
  </div>
  <div class="abs frames-row">
    <svg width="44" height="18" viewBox="0 0 44 18"><path d="M2 4H42" stroke="var(--navy)" stroke-width="2"/><ellipse cx="11" cy="10" rx="9" ry="7" fill="var(--navy)"/><ellipse cx="33" cy="10" rx="9" ry="7" fill="var(--navy)"/></svg>
    <span>Over <b>1,000</b> Designer Frames &amp; Sunglasses</span>
  </div>
  <div class="abs brands">
    <span>VELLANO</span><span>MARCELLE</span><span>LUMIÈRE</span><span>ARCLIGHT</span>
    <span>TIDEWELL</span><span>Hartwell &amp; Co.</span><span>ELLIS GRANT</span><span>AURELIO</span>
    <span>JUNE AVERY</span><span>Summit</span><span>SUNMARK</span><span>Coral Bay &amp; More</span>
  </div>
  <div class="abs contact-band">
    <div class="abs site">www.ClearviewEyeStudio.com</div>
    <div class="abs contact-rule"></div>
    <div class="abs cta">Call or Text for<br>Appointment</div>
    <div class="abs phone">555.014.2200</div>
  </div>
  <div class="abs stripe"><i style="background:var(--stripe-grey)"></i><i style="background:var(--gold)"></i><i style="background:var(--stripe-brown)"></i><i style="background:var(--stripe-green)"></i><i style="background:var(--stripe-blue)"></i></div>
</section>

<section class="card card-back">
  <svg class="abs gold-wave" width="295" height="48" viewBox="0 0 295 48">
    <path d="M0 0H295V40C270 30 250 34 225 38C195 42 170 36 148 32C120 28 100 36 75 40C50 44 25 34 0 32Z" fill="var(--gold)"/>
  </svg>
  <div class="abs back-title">Meet our Doctors</div>

  <div class="doctor" style="left:15px;top:38px"><div class="doctor-photo" role="img" aria-label="Portrait photo of Dr. Laura Whitfield"></div>Dr. Laura Whitfield, O.D.</div>
  <div class="doctor" style="left:148px;top:38px"><div class="doctor-photo" role="img" aria-label="Portrait photo of Dr. Megan Ashford"></div>Dr. Megan Ashford, O.D.</div>
  <div class="doctor" style="left:15px;top:173px"><div class="doctor-photo" role="img" aria-label="Portrait photo of Dr. Daniel Reyes"></div>Dr. Daniel Reyes, O.D.</div>
  <div class="doctor" style="left:148px;top:173px"><div class="doctor-photo" role="img" aria-label="Portrait photo of Dr. Nadia Farrow"></div>Dr. Nadia Farrow, O.D.</div>

  <div class="abs services-band">Our Services</div>
  <div class="abs services">
    <div class="service"><svg width="26" height="16" viewBox="0 0 26 16"><path d="M1 8C6 1 20 1 25 8C20 15 6 15 1 8Z" fill="none" stroke="var(--gold)" stroke-width="1.8"/><circle cx="13" cy="8" r="4" fill="var(--gold)"/></svg>Comprehensive<br>Eye Exams</div>
    <div class="service"><svg width="26" height="16" viewBox="0 0 26 16"><path d="M1 8C6 1 20 1 25 8C20 15 6 15 1 8Z" fill="none" stroke="var(--gold)" stroke-width="1.8"/><circle cx="13" cy="8" r="4" fill="var(--gold)"/></svg>Dry Eye<br>&amp; Allergy</div>
    <div class="service"><svg width="26" height="16" viewBox="0 0 26 16"><path d="M1 8C6 1 20 1 25 8C20 15 6 15 1 8Z" fill="none" stroke="var(--gold)" stroke-width="1.8"/><circle cx="13" cy="8" r="4" fill="var(--gold)"/></svg>Speciality Contact<br>Lens Service</div>
    <div class="service"><svg width="26" height="16" viewBox="0 0 26 16"><circle cx="13" cy="8" r="7" fill="none" stroke="var(--gold)" stroke-width="1.8"/><path d="M14 3L10 9H14L12 13" stroke="var(--gold)" stroke-width="1.6" fill="none"/></svg>Migraine &amp;<br>Headache</div>
    <div class="service"><svg width="26" height="16" viewBox="0 0 26 16"><path d="M1 8C6 1 20 1 25 8C20 15 6 15 1 8Z" fill="none" stroke="var(--gold)" stroke-width="1.8"/><circle cx="13" cy="8" r="4" fill="var(--gold)"/></svg>Pediatric<br>Exams</div>
    <div class="service"><svg width="26" height="16" viewBox="0 0 26 16"><path d="M1 8H25M13 1V15" stroke="var(--gold)" stroke-width="1.4"/><circle cx="13" cy="8" r="4" fill="none" stroke="var(--gold)" stroke-width="1.8"/></svg>Eye Muscle<br>Alignment</div>
    <div class="service"><svg width="26" height="16" viewBox="0 0 26 16"><path d="M1 8C6 1 20 1 25 8C20 15 6 15 1 8Z" fill="none" stroke="var(--gold)" stroke-width="1.8"/><circle cx="13" cy="8" r="4" fill="var(--gold)"/></svg>Surgery<br>Co-Management</div>
    <div class="service"><svg width="26" height="16" viewBox="0 0 26 16"><path d="M1 8C6 1 20 1 25 8C20 15 6 15 1 8Z" fill="none" stroke="var(--gold)" stroke-width="1.8"/><path d="M10 8H16M13 5V11" stroke="var(--gold)" stroke-width="1.8"/></svg>Eye Injuries &amp;<br>Infections</div>
    <div class="service tall"><svg width="26" height="16" viewBox="0 0 26 16"><path d="M1 8C6 1 20 1 25 8C20 15 6 15 1 8Z" fill="none" stroke="var(--gold)" stroke-width="1.8"/><circle cx="13" cy="8" r="4" fill="var(--gold)"/></svg>Cataract,<br>Glaucoma, Macular<br>Degeneration</div>
    <div class="service tall"><svg width="26" height="16" viewBox="0 0 26 16"><path d="M1 8C6 1 20 1 25 8C20 15 6 15 1 8Z" fill="none" stroke="var(--gold)" stroke-width="1.8"/><path d="M10 8H16M13 5V11" stroke="var(--gold)" stroke-width="1.8"/></svg>Ocular Disease<br>Management</div>
  </div>

  <div class="abs navy-base"></div>
  <div class="abs feature-box">
    <div class="feature"><svg width="24" height="26" viewBox="0 0 24 26"><circle cx="12" cy="7" r="6" fill="none" stroke="var(--navy)" stroke-width="1.5"/><path d="M2 25C2 17 6 14 12 14C18 14 22 17 22 25" fill="none" stroke="var(--navy)" stroke-width="1.5"/></svg>Complete Eye Care<br>For the<br>Entire Family</div>
    <div class="feature"><svg width="24" height="26" viewBox="0 0 24 26"><path d="M12 25C12 25 3 15 3 9A9 9 0 0 1 21 9C21 15 12 25 12 25Z" fill="none" stroke="var(--navy)" stroke-width="1.5"/><circle cx="12" cy="9" r="3" fill="none" stroke="var(--navy)" stroke-width="1.5"/></svg>Hometown<br>Owned &amp;<br>Operated</div>
    <div class="feature"><svg width="26" height="26" viewBox="0 0 26 26"><rect x="2" y="4" width="22" height="20" rx="2" fill="none" stroke="var(--navy)" stroke-width="1.5"/><path d="M7 1V7M19 1V7M2 10H24" stroke="var(--navy)" stroke-width="1.5"/><path d="M8 17L11 20L18 13" fill="none" stroke="var(--navy)" stroke-width="1.5"/></svg>Walk-ins<br>Welcome!</div>
  </div>
  <div class="abs address">418 Meadow Ridge Dr, Brookfield TX 77000</div>
  <div class="abs hours">Hours: Mon–Thu 8-5. Fri 9-4:30</div>
  <div class="abs tagline">Complete Eye Care For the Entire Family</div>
  <div class="abs stripe"><i style="background:var(--stripe-grey)"></i><i style="background:var(--gold)"></i><i style="background:var(--stripe-brown)"></i><i style="background:var(--stripe-green)"></i><i style="background:var(--stripe-blue)"></i></div>
</section>

</body>
</html>
```